Letterhead to Introduce a 'Sister' Company.

What I am needing is a design for a letter head to introduce our current customers base of (KT Alarm) customers to our new service, 'Kestrel Tide Solar Brokers'

```html
<!DOCTYPE html>
<html lang="en">
<head>
<meta charset="utf-8">
<title>Kestrel Tide Solar Brokers Letterhead</title>
<link rel="stylesheet" href="https://fonts.googleapis.com/css2?family=Montserrat:wght@500;700;800&family=Open+Sans:wght@400;600&display=swap">
<style>
  :root {
    --backdrop: #ecebe8;
    --paper: #ffffff;
    --orange: #f5a21b;
    --blue: #2b6cb3;
    --ink: #3a3a3a;
    --muted: #8a8a8a;
    --shape-a: #f1f1f1;
    --shape-b: #e6e6e6;
  }
  * { box-sizing: border-box; margin: 0; padding: 0; }
  html, body { width: 713px; height: 1200px; overflow: hidden; }
  body {
    background: var(--backdrop);
    font-family: "Open Sans", Arial, sans-serif;
    color: var(--ink);
    position: relative;
  }
  .letterhead {
    position: absolute;
    left: 46px; top: 162px;
    width: 620px; height: 877px;
    background: var(--paper);
    box-shadow: 0 4px 18px rgba(0,0,0,0.12);
    overflow: hidden;
  }
  .brand {
    position: absolute; left: 44px; top: 36px;
    display: flex; align-items: center; gap: 9px;
  }
  .brand-mark { width: 30px; height: 30px; background: var(--orange); border-radius: 50%; }
  .brand-name {
    font-family: "Montserrat", Arial, sans-serif; font-weight: 800;
    color: var(--blue); font-size: 15px; line-height: 1.1; letter-spacing: 0.5px;
    text-transform: uppercase;
  }
  .brand-name small { display: block; font-size: 9px; letter-spacing: 1.5px; }
  .brand-name em { display: block; font-style: normal; font-size: 8px; letter-spacing: 1px; }

  .sidebar { position: absolute; left: 44px; top: 130px; width: 130px; font-size: 8px; line-height: 1.5; }
  .sidebar .label { color: var(--muted); }
  .sidebar .name { font-family: "Montserrat", Arial, sans-serif; font-weight: 700; color: var(--blue); text-transform: uppercase; font-size: 8.5px; }
  .sidebar .block { margin-bottom: 22px; }
  .contact { display: flex; flex-direction: column; align-items: flex-start; gap: 4px; margin-bottom: 26px; }
  .contact .icon { width: 22px; height: 22px; border-radius: 50%; background: var(--orange); display: flex; align-items: center; justify-content: center; }
  .contact span { font-size: 7.5px; color: var(--ink); }

  .letter { position: absolute; left: 210px; top: 130px; width: 366px; font-size: 8px; line-height: 1.65; }
  .letter .date { margin-bottom: 30px; }
  .letter .greeting { font-family: "Montserrat", Arial, sans-serif; font-weight: 700; color: var(--blue); margin-bottom: 6px; }
  .letter p { margin-bottom: 14px; text-align: justify; color: #555; }

  .shapes { position: absolute; left: 0; bottom: 0; width: 620px; height: 260px; }
  .signature { position: absolute; right: 44px; bottom: 64px; width: 150px; border-top: 1px solid #9a9a9a; padding-top: 6px; text-align: right; font-family: "Montserrat", Arial, sans-serif; font-weight: 500; font-size: 13px; color: var(--ink); }
</style>
</head>
<body>
  <main class="letterhead">
    <svg class="shapes" viewBox="0 0 620 260" aria-hidden="true">
      <polygon points="0,120 200,260 0,260" fill="var(--shape-a)"/>
      <polygon points="0,180 360,260 120,260" fill="var(--shape-b)" opacity="0.6"/>
      <polygon points="180,260 460,90 620,60 620,260" fill="var(--shape-a)"/>
      <polygon points="330,260 620,150 620,260" fill="var(--shape-b)" opacity="0.7"/>
    </svg>

    <header class="brand">
      <div class="brand-mark"></div>
      <div class="brand-name">Kestrel Tide<small>Solar Brokers</small><em>by KT Alarm</em></div>
    </header>

    <aside class="sidebar">
      <div class="block">
        <div class="label">To</div>
        <div class="name">Dana Whitlow</div>
        <div class="label">Manager/Director</div>
      </div>
      <div class="block">
        <div class="name">Kestrel Tide</div>
        <div>48 Harbour Lane,<br>Westford</div>
      </div>
      <div class="contact">
        <div class="icon"><svg width="12" height="12" viewBox="0 0 24 24"><rect x="3" y="6" width="18" height="12" rx="1" fill="none" stroke="#fff" stroke-width="2"/><path d="M3 7l9 6 9-6" fill="none" stroke="#fff" stroke-width="2"/></svg></div>
        <span>hello@kestreltide.co</span>
      </div>
      <div class="contact">
        <div class="icon"><svg width="12" height="12" viewBox="0 0 24 24"><path d="M6 3l4 4-2 3c1 2 3 4 5 5l3-2 4 4-3 3C10 20 4 14 3 6z" fill="#fff"/></svg></div>
        <span>+00 123 456 789<br>+00 987 654 321</span>
      </div>
      <div class="contact">
        <div class="icon"><svg width="12" height="12" viewBox="0 0 24 24"><circle cx="12" cy="12" r="8" fill="none" stroke="#fff" stroke-width="2"/><path d="M4 12h16M12 4c3 3 3 13 0 16M12 4c-3 3-3 13 0 16" fill="none" stroke="#fff" stroke-width="1.5"/></svg></div>
        <span>www.kestreltide.co</span>
      </div>
    </aside>

    <section class="letter">
      <div class="date">17 February 2021</div>
      <div class="greeting">Hello</div>
      <p>We are writing to let you know about a new service from the team you already trust. Kestrel Tide Solar Brokers helps homes and businesses compare solar options, find fair pricing and choose installers with proven records, all with the same care you expect from KT Alarm.</p>
      <p>Our brokers review your energy use, roof space and budget, then present clear quotes side by side. There is no cost for the review and no obligation to proceed, so you can decide in your own time.</p>
      <p>As a valued alarm customer, you will receive priority booking and a loyalty discount on any system arranged through us this year. Simply reply to this letter or call our office to book a visit.</p>
      <p>Thank you for your continued support. We look forward to helping you save on power bills.</p>
    </section>

    <div class="signature">Signature</div>
  </main>
</body>
</html>
```